Flyer-Design für trommel-wissen
Zielgruppe
Website und Onlineshop rund um die irische Rahmentrommel 'bodhrán'. Wir bieten Informationen, Kaufberatung und einen Onlineshop. Wir sind auf Qualitätsinstrumente spezialisiert und verkaufen keine billigen Instrumente aus Fernost.
Aufgabenstellung
Wir haben die Website komplett neu gestaltet und brauchen nun einen neuen Flyer im Stil der Website. Die Adresse ist www.trommel-wissen.de Es müsste also auf den Bildern und ungefähr dem Design der Website beruhen. Die Bilder kann ich dann natürlich zur Verfügung stellen. Beim Format würde ich gerne etwas kleineres längliches nehmen und auf 300er Recycling Papier drucken. Hatte vorher DIN lang, aber ich habe hier Flyer in 14*6,5 cm gesehen, die fand ich auch schön.
Die Seite ist deutsch und englisch, daher sollte der Flyer eine Seite deutsch, eine Seite englisch haben.

```html
<!DOCTYPE html>
<html lang="de">
<head>
<meta charset="utf-8">
<title>trommel-wissen – Flyer</title>
<link href="https://fonts.googleapis.com/css2?family=Fira+Sans:wght@300;400;500;600;700&family=Fira+Sans+Condensed:wght@700&display=swap" rel="stylesheet">
<style>
  :root {
    --brand-red: #a8281c;
    --ink: #111111;
    --grey-text: #555555;
    --paper: #ffffff;
    --frame: #8a8a8a;
    --mark-dark: #1c1c1c;
  }
  * { margin: 0; padding: 0; box-sizing: border-box; }
  html, body { width: 1200px; height: 2584px; overflow: hidden; background: var(--paper); }
  .flyer {
    position: relative;
    width: 1200px;
    height: 2584px;
    background: var(--paper);
    border: 2px solid var(--frame);
    overflow: hidden;
    font-family: "Fira Sans", sans-serif;
    color: var(--ink);
  }
  .hero { position: absolute; left: 0; top: 0; width: 1200px; height: 719px; display: block; }

  .brand { position: absolute; left: 130px; top: 781px; width: 950px; height: 140px; }
  .brand-square {
    position: absolute; left: 0; top: 0; width: 136px; height: 136px;
    background: var(--mark-dark); border-radius: 14px;
  }
  .brand-name {
    position: absolute; left: 158px; top: -18px;
    font-family: "Fira Sans", sans-serif; font-weight: 700;
    font-size: 106px; line-height: 1; color: var(--brand-red);
    letter-spacing: -1px; white-space: nowrap;
  }
  .brand-tagline {
    position: absolute; left: 168px; top: 100px;
    font-family: "Fira Sans Condensed", sans-serif; font-weight: 700;
    font-size: 28px; letter-spacing: 5.8px; color: var(--ink); white-space: nowrap;
  }

  .intro {
    position: absolute; left: 131px; top: 1002px; width: 1000px;
    font-size: 51px; font-weight: 500; line-height: 62.5px; letter-spacing: 0.4px; color: var(--ink);
  }

  .section-icon { position: absolute; display: block; }
  .section-title {
    position: absolute; font-size: 57px; font-weight: 500; line-height: 1; color: var(--ink); white-space: nowrap;
  }
  .features {
    position: absolute; list-style: none;
    font-size: 51px; font-weight: 300; line-height: 62.5px; letter-spacing: 0.4px; color: var(--grey-text);
  }
  .features li { position: relative; padding-left: 75px; white-space: nowrap; }
  .features li svg { position: absolute; left: 0; top: 18px; width: 44px; height: 34px; }

  .info-title { left: 258px; top: 1356px; }
  .info-list { left: 133px; top: 1472px; width: 1000px; }
  .shop-title { left: 253px; top: 1809px; }
  .shop-list { left: 128px; top: 1927px; width: 1040px; }

  .web-address {
    position: absolute; right: 130px; top: 2267px;
    font-size: 46px; font-weight: 500; line-height: 1; color: var(--ink);
  }
  .divider { position: absolute; left: 128px; top: 2377px; width: 942px; height: 5px; background: var(--brand-red); }

  .partner {
    position: absolute; left: 125px; top: 2434px;
    font-family: "Fira Sans", sans-serif; font-weight: 600; color: var(--ink); text-align: center; line-height: 1;
  }
  .partner-name { font-size: 48px; letter-spacing: 2px; }
  .partner-tier { font-size: 34px; letter-spacing: 2.5px; margin-top: 6px; }
  .distributor {
    position: absolute; right: 130px; top: 2424px;
    font-family: "Fira Sans", sans-serif; font-weight: 600; font-size: 80px; letter-spacing: 3px; line-height: 1; color: var(--ink);
  }
</style>
</head>
<body>
<div class="flyer">

  <svg class="hero" viewBox="0 0 768 460" preserveAspectRatio="none" role="img" aria-label="Foto: Reihe handgefertigter Bodhráns mit rotem, blauem und holzfarbenem Rahmen">
    <defs>
      <linearGradient id="drumTones" x1="0" y1="0" x2="1" y2="0">
        <stop offset="0" stop-color="#c2391f"/>
        <stop offset="0.3" stop-color="#d4552f"/>
        <stop offset="0.42" stop-color="#1d2530"/>
        <stop offset="0.55" stop-color="#2e6f8e"/>
        <stop offset="0.66" stop-color="#b89a72"/>
        <stop offset="0.8" stop-color="#9a4a26"/>
        <stop offset="1" stop-color="#d9b27c"/>
      </linearGradient>
    </defs>
    <path d="M0 265 L0 360 Q380 520 768 305 L768 265 Z" fill="var(--brand-red)"/>
    <path d="M0 0 H768 V298 Q430 470 0 275 Z" fill="url(#drumTones)"/>
  </svg>

  <div class="brand">
    <div class="brand-square"></div>
    <div class="brand-name">trommel-wissen</div>
    <div class="brand-tagline">ALLES RUND UM DIE IRISCHE RAHMENTROMMEL</div>
  </div>

  <p class="intro">Wir bieten individuelle Beratung,<br>die auf einer 30-jährigen Erfahrung<br>im professionellem Bodhránspiel<br>und Unterricht aufbaut.</p>

  <svg class="section-icon" style="left:128px;top:1326px;width:91px;height:88px" viewBox="0 0 60 58" fill="none" stroke="var(--brand-red)" stroke-width="2.6" aria-hidden="true">
    <path d="M4 16 L30 3 L56 16 Z"/>
    <rect x="4" y="16" width="52" height="5"/>
    <path d="M11 24 V46 M19 24 V46 M27 24 V46 M35 24 V46 M43 24 V46 M50 24 V46"/>
    <rect x="4" y="47" width="52" height="4"/>
    <rect x="1.5" y="52" width="57" height="4.5"/>
  </svg>
  <h2 class="section-title info-title">Die irische Rahmentrommel</h2>
  <ul class="features info-list">
    <li><svg viewBox="0 0 44 34"><path d="M3 17 L16 29 L41 4" fill="none" stroke="var(--brand-red)" stroke-width="4.5"/></svg>Alles über die Bodhrán</li>
    <li><svg viewBox="0 0 44 34"><path d="M3 17 L16 29 L41 4" fill="none" stroke="var(--brand-red)" stroke-width="4.5"/></svg>Ratgeber zum Bodhránkauf</li>
    <li><svg viewBox="0 0 44 34"><path d="M3 17 L16 29 L41 4" fill="none" stroke="var(--brand-red)" stroke-width="4.5"/></svg>Infos über Tipper, Geschichte<br>und Konstruktion</li>
  </ul>

  <svg class="section-icon" style="left:125px;top:1789px;width:84px;height:80px" viewBox="0 0 54 52" fill="none" stroke="var(--brand-red)" stroke-width="2.6" aria-hidden="true">
    <rect x="2" y="2" width="50" height="48"/>
    <path d="M2 16 H52 M10 2 V16 M18 2 V16 M26 2 V16 M34 2 V16 M42 2 V16"/>
    <rect x="8" y="24" width="20" height="14"/>
    <path d="M34 50 V24 H46 V50"/>
  </svg>
  <h2 class="section-title shop-title">Online Shop</h2>
  <ul class="features shop-list">
    <li><svg viewBox="0 0 44 34"><path d="M3 17 L16 29 L41 4" fill="none" stroke="var(--brand-red)" stroke-width="4.5"/></svg>Handgefertigte Bodhráns und Tipper</li>
    <li><svg viewBox="0 0 44 34"><path d="M3 17 L16 29 L41 4" fill="none" stroke="var(--brand-red)" stroke-width="4.5"/></svg>ExpressKonfigurator zum<br>Konfigurieren individueller Bodhráns</li>
    <li><svg viewBox="0 0 44 34"><path d="M3 17 L16 29 L41 4" fill="none" stroke="var(--brand-red)" stroke-width="4.5"/></svg>Taschen, Zubehör, Lernmaterial<br>und CDs</li>
  </ul>

  <div class="web-address">www.trommel-wissen.de</div>
  <div class="divider"></div>

  <div class="partner">
    <div class="partner-name">KESSELMANN DRUMS</div>
    <div class="partner-tier">PREMIUM PARTNER</div>
  </div>
  <div class="distributor">mirvel</div>

</div>
</body>
</html>
```